Honigmüsli Etikett
Zielgruppe
Wir sind eine Imkerei und erzeugen Regionale, Nachhaltige und Biologisch wertvolle Produkte bei denen die umwelt und der umweltschutz sowie die Qualität im vordergrund stehen.
Aufgabenstellung
Der Kunde soll die Natührlichkeit des Produktes im Etikett erkennen.
Es handelt sich hierbei um eine Müslitüte aus braunem Papier mit großem Sichtfenster.
Das Frontetikett sollte nur die wichtigsten und prignanten Dinge aufweisen und das Rückenetikett dann die restlichen Dinge.
Im anhang befindet sich bereits das aktuelle Etikett, welches so im moment auf den Tüten zu sehen ist. Dieses soll nun aber modernisiert und aufgefrischt werden.
Es handelt sich um ein mit Honig gesüßtes Müsli, welches ausschließlich auf gesunde und natührliche Stoffe setzt, dies soll im Etikett wiedergespiegelt werden.
Die Etiketten sind derzeit in den Maßen: 7,5cm x 5cm (Front) und 8,5cm x 6cm (Rücken)
dies ist aber kein muss und kann wenn es möglichkeiten der Etikettgestaltungen gibt die mehr Platz benötigen auch angepasst werden. Das Gesamtbild mit dem großen Fenster sollte allerdings harmonieren und nicht durch ein zu großes Etikett überlagert werden.

```html
<!DOCTYPE html>
<html lang="de">
<head>
<meta charset="utf-8">
<title>Knuspermüsli Etiketten</title>
<link rel="stylesheet" href="https://fonts.googleapis.com/css2?family=Open+Sans:wght@400;700;800&family=Yellowtail&family=Oswald:wght@300&display=swap">
<style>
  :root {
    --bg: #f4f2ee;
    --ink: #1f1f1f;
    --paper: #ffffff;
    --honey: #ecb84a;
    --wheat-light: #f3e3b8;
    --wheat-mid: #d9a84a;
    --wheat-dark: #a8772a;
    --red: #b3161b;
    --text: #333333;
  }
  * { box-sizing: border-box; margin: 0; padding: 0; }
  html, body { width: 1151px; height: 1200px; overflow: hidden; }
  body { background: var(--bg); font-family: "Open Sans", sans-serif; color: var(--text); position: relative; }

  .label { position: absolute; overflow: hidden; }

  /* Front label */
  .front { left: 150px; top: 210px; width: 380px; height: 780px; background: var(--paper); }
  .front .field {
    position: absolute; left: 0; top: 0; width: 100%; height: 331px;
    background: linear-gradient(180deg, var(--wheat-light) 0%, var(--wheat-mid) 45%, var(--wheat-dark) 100%);
  }
  .brand-box {
    position: absolute; left: 127px; top: 0; width: 126px; height: 113px;
    background: var(--ink); color: #fff;
    display: flex; flex-direction: column; align-items: center; justify-content: center; gap: 6px;
  }
  .brand-box .ring { width: 38px; height: 38px; border: 2px solid #fff; border-radius: 50%; }
  .brand-box .name { font-size: 12px; font-weight: 700; letter-spacing: 1px; }
  .product-title {
    position: absolute; left: 0; top: 132px; width: 100%; text-align: center;
    font-family: "Yellowtail", cursive; font-size: 50px; line-height: 46px; color: var(--ink);
  }
  .tagline {
    position: absolute; left: 43px; right: 43px; top: 244px;
    display: flex; align-items: center; gap: 6px;
    color: var(--red); font-weight: 800; font-size: 13px; letter-spacing: 2px; white-space: nowrap;
  }
  .tagline::before, .tagline::after { content: ""; flex: 1; height: 1px; background: var(--ink); }
  .origin {
    position: absolute; left: 100px; top: 268px; transform: rotate(-6deg);
    font-family: "Yellowtail", cursive; font-size: 23px; color: #fff;
  }
  .weight { position: absolute; right: 36px; top: 304px; font-size: 14px; font-weight: 700; color: var(--ink); }
  .web-band {
    position: absolute; left: 0; width: 100%; background: var(--ink); color: #fff;
    display: flex; align-items: center; justify-content: center;
    font-size: 15px; letter-spacing: 2.5px;
  }
  .front .web-band { top: 331px; height: 45px; }
  .front .window {
    position: absolute; left: 0; top: 376px; width: 100%; height: 404px;
    background: radial-gradient(circle at 40% 55%, #6b2a2a 0%, #b98a52 35%, #d8c29a 65%, #8b6a3d 100%);
  }

  /* Back label */
  .back { left: 600px; top: 457px; width: 400px; height: 533px; background: var(--paper); text-align: center; }
  .back .brand-box { left: 144px; width: 112px; height: 99px; }
  .back .brand-box .ring { width: 34px; height: 34px; }
  .brand-row {
    position: absolute; left: 0; top: 106px; width: 100%;
    display: flex; align-items: center; justify-content: center; gap: 8px;
    font-size: 17px; font-weight: 700; color: var(--ink);
  }
  .brand-row .ring { width: 30px; height: 30px; border: 2px solid var(--ink); border-radius: 50%; }
  .product-band {
    position: absolute; left: 0; top: 183px; width: 100%; height: 53px; background: var(--honey);
    display: flex; flex-direction: column; justify-content: center;
  }
  .product-band .name { font-size: 17px; font-weight: 800; letter-spacing: 3px; color: var(--ink); line-height: 20px; }
  .product-band .sub { font-size: 12px; letter-spacing: 1.5px; color: #fff; line-height: 16px; }
  .ingredients { position: absolute; left: 30px; right: 30px; top: 245px; font-size: 15px; line-height: 20px; }
  .ingredients h3 { font-size: 15px; font-weight: 700; color: var(--ink); }
  .best-before { position: absolute; left: 0; top: 350px; width: 100%; font-size: 15px; font-weight: 700; color: var(--ink); }
  .best-before .date { font-family: "Oswald", sans-serif; font-weight: 300; font-size: 13px; margin-left: 6px; }
  .rule { position: absolute; left: 86px; right: 86px; top: 404px; height: 1px; background: var(--ink); }
  .address { position: absolute; left: 0; top: 418px; width: 100%; font-size: 15px; line-height: 20px; font-style: normal; }
  .address strong { color: var(--ink); }
  .back .web-band { top: 494px; height: 39px; font-size: 14px; }
</style>
</head>
<body>
  <section class="label front">
    <div class="field" role="img" aria-label="Foto eines goldenen Weizenfelds"></div>
    <div class="brand-box"><span class="ring"></span><span class="name">LINDENAU</span></div>
    <h1 class="product-title">Lindenaus<br>Knuspermüsli</h1>
    <p class="tagline">MIT HONIG VEREDELT</p>
    <p class="origin">Honig aus eigener Imkerei</p>
    <p class="weight">500 g</p>
    <div class="web-band">WWW.LINDENAU-IMKEREI.DE</div>
    <div class="window" role="img" aria-label="Nahaufnahme von Knuspermüsli mit Haferflocken, Nüssen und getrockneten Beeren"></div>
  </section>

  <section class="label back">
    <div class="brand-box"><span class="ring"></span><span class="name">LINDENAU</span></div>
    <div class="brand-row"><span class="ring"></span><span>Imkerei Lindenau</span></div>
    <div class="product-band">
      <span class="name">KNUSPERMÜSLI</span>
      <span class="sub">MIT HONIG VEREDELT</span>
    </div>
    <div class="ingredients">
      <h3>Zutaten:</h3>
      <p>Haferflocken, Honig, Sonnenblumenkerne, Öl, Mandeln, Rosinen, getrocknete Weinbeeren</p>
    </div>
    <p class="best-before">Mindestens haltbar bis: <span class="date">01.06.2020</span></p>
    <div class="rule"></div>
    <address class="address">
      <strong>Imkerei Lindenau</strong><br>
      Lindenweg 7 · 34999 Auenfeld<br>
      Telefon +49 12 34 - 56 78 90
    </address>
    <div class="web-band">WWW.LINDENAU-IMKEREI.DE</div>
  </section>
</body>
</html>
```